Sales Flyer for Outdoor Kitchens

Looks to have a trifold flyer designed based off website content / projects. Use www.brickleafyardworks.com for content

```html
<!DOCTYPE html>
<html lang="en">
<head>
<meta charset="utf-8">
<title>Brickleaf Yardworks – Trifold Brochure</title>
<link rel="stylesheet" href="https://fonts.googleapis.com/css2?family=Montserrat:wght@400;500;600;700;800&display=swap">
<style>
  :root{
    --green:#3bb54a;
    --blue:#1f6fc5;
    --blue-light:#2d86d6;
    --ink:#2f3133;
    --paper:#f3f4f4;
    --stage:#a4a5a6;
    --white:#ffffff;
  }
  *{box-sizing:border-box;margin:0;padding:0}
  html,body{width:1200px;height:3404px;overflow:hidden}
  body{background:var(--stage);font-family:"Montserrat",sans-serif;color:var(--ink);position:relative}
  .spread{position:absolute;left:30px;width:1089px;height:768px;background:var(--paper);box-shadow:0 6px 16px rgba(0,0,0,.28);overflow:hidden;transform:scale(1.0468);transform-origin:0 0}
  .spread--outer{top:640px}
  .spread--inner{top:1780px}
  .spread svg.art{position:absolute;left:0;top:0}
  .abs{position:absolute}
  .brand{display:flex;align-items:center;gap:10px;color:var(--green);font-weight:700;letter-spacing:.5px;line-height:1.05}
  .brand__dot{width:34px;height:34px;border-radius:50%;background:var(--green);flex:none}
  .brand__name{font-size:20px}
  .brand--small .brand__dot{width:18px;height:18px}
  .brand--small .brand__name{font-size:11px}
  .heading{font-weight:800;color:var(--blue);line-height:1.15;text-transform:uppercase}
  .heading--green{color:var(--green)}
  .sub{font-weight:500;font-size:16.5px;line-height:1.35;color:var(--ink)}
  .body{font-size:11.6px;line-height:1.42;color:var(--ink);text-align:justify}
  .tab{background:var(--blue);color:var(--white);font-weight:700;font-size:14px;text-align:center;border-radius:6px 6px 0 0;padding:3px 0}
  .phone-bar{background:var(--green);color:var(--white);font-weight:700;display:flex;align-items:center;justify-content:center;gap:10px}
  .phone-bar svg{flex:none}
  .contact{font-size:14.5px;font-weight:500;text-align:center;color:var(--ink);line-height:1.35}
  .process{background:var(--green);padding:22px 20px 0 20px;color:var(--white)}
  .process__title{font-weight:800;font-size:16px;line-height:1.35;margin-bottom:14px}
  .process__list{list-style:none}
  .process__list li{display:flex;align-items:center;gap:8px;font-size:12.6px;font-weight:500;height:30px}
  .process__num{width:20px;height:20px;border-radius:50%;background:var(--white);color:var(--blue);font-size:10px;font-weight:800;display:flex;align-items:center;justify-content:center}
</style>
</head>
<body>

<section class="spread spread--outer" aria-label="Brochure outside spread">
  <svg class="art" width="1089" height="768" viewBox="0 0 1089 768">
    <defs>
      <linearGradient id="paperTone" x1="0" y1="0" x2="0" y2="1">
        <stop offset="0" stop-color="#f4f5f5"/><stop offset="1" stop-color="#e3e6e6"/>
      </linearGradient>
      <linearGradient id="pavilionWhite" x1="0" y1="0" x2="0" y2="1">
        <stop offset="0" stop-color="#7fa9cf"/><stop offset=".3" stop-color="#e9ecef"/><stop offset=".6" stop-color="#8a6a4a"/><stop offset="1" stop-color="#4a4038"/>
      </linearGradient>
      <linearGradient id="pavilionWood" x1="0" y1="0" x2="0" y2="1">
        <stop offset="0" stop-color="#3f6a32"/><stop offset=".25" stop-color="#8f6a4e"/><stop offset=".55" stop-color="#a8612e"/><stop offset=".8" stop-color="#5f8f3a"/><stop offset="1" stop-color="#9aa39a"/>
      </linearGradient>
      <linearGradient id="pavilionCut" x1="0" y1="0" x2="0" y2="1">
        <stop offset="0" stop-color="#7d8590"/><stop offset=".3" stop-color="#f2f0ec"/><stop offset=".65" stop-color="#9b6a42"/><stop offset="1" stop-color="#54585c"/>
      </linearGradient>
    </defs>
    <rect width="1089" height="768" fill="url(#paperTone)" role="img" aria-label="Faint backyard tree backdrop"/>
    <path role="img" aria-label="Photo: white pavilion with bar seating and outdoor kitchen" d="M0 0H363V230C300 250 250 262 200 275C130 292 60 300 0 306Z" fill="url(#pavilionWhite)"/>
    <path d="M363 232C300 250 240 268 190 282" fill="none" stroke="var(--green)" stroke-width="7"/>
    <polygon role="img" aria-label="Photo: white gable pavilion over dining set" points="193,768 193,612 300,540 462,490 620,540 722,612 722,768" fill="url(#pavilionCut)"/>
    <path d="M0 590C40 560 120 560 170 600" fill="none" stroke="var(--green)" stroke-width="7"/>
    <circle cx="108" cy="654" r="82" fill="var(--white)"/>
    <path role="img" aria-label="Photo: cedar pavilion with fire pit and lawn" d="M726 172C850 150 980 140 1089 110V470C960 470 820 500 726 530Z" fill="url(#pavilionWood)"/>
    <path d="M726 168C850 146 980 136 1089 106" fill="none" stroke="var(--blue)" stroke-width="9"/>
    <path d="M700 545C820 500 960 470 1089 466" fill="none" stroke="var(--green)" stroke-width="9"/>
  </svg>

  <div class="abs heading" style="left:24px;top:310px;font-size:30px;line-height:1.3">Who<br><span style="color:var(--green)">We Are</span></div>
  <p class="abs body" style="left:24px;top:397px;width:266px">With over a decade of experience in the industry, Dale Whitmore, the owner and operator of BYW, has become a well-known name in the Houston area. His passion for outdoor living spaces, coupled with his keen eye for design and attention to detail, has led him to create some of the most stunning and functional outdoor spaces for his clients.</p>
  <div class="abs brand brand--small" style="left:48px;top:640px"><span class="brand__dot"></span><span class="brand__name">BRICKLEAF<br>YARDWORKS</span></div>

  <div class="abs brand" style="left:450px;top:78px"><span class="brand__dot"></span><span class="brand__name">BRICKLEAF<br>YARDWORKS</span></div>
  <div class="abs tab" style="left:400px;top:206px;width:236px">REQUEST CONSULTATION</div>
  <div class="abs phone-bar" style="left:356px;top:229px;width:328px;height:48px;font-size:29px">
    <svg width="24" height="24" viewBox="0 0 24 24"><path fill="#fff" d="M6.6 10.8a15.1 15.1 0 0 0 6.6 6.6l2.2-2.2a1 1 0 0 1 1-.25 11.4 11.4 0 0 0 3.6.57 1 1 0 0 1 1 1V20a1 1 0 0 1-1 1A17 17 0 0 1 3 4a1 1 0 0 1 1-1h3.5a1 1 0 0 1 1 1c0 1.25.2 2.45.57 3.57a1 1 0 0 1-.25 1z"/></svg>
    555-014-2297
  </div>
  <svg class="abs" style="left:470px;top:313px" width="142" height="40" viewBox="0 0 142 40" aria-hidden="true">
    <circle cx="20" cy="20" r="19" fill="var(--green)"/>
    <rect x="10" y="13" width="20" height="14" rx="2" fill="#fff"/>
    <path d="M10 14l10 8 10-8" fill="none" stroke="var(--green)" stroke-width="2"/>
    <circle cx="71" cy="20" r="19" fill="var(--green)"/>
    <path d="M71 9a7 7 0 0 1 7 7c0 5-7 14-7 14s-7-9-7-14a7 7 0 0 1 7-7z" fill="#fff"/>
    <circle cx="71" cy="16" r="2.6" fill="var(--green)"/>
    <circle cx="122" cy="20" r="19" fill="var(--green)"/>
    <circle cx="122" cy="20" r="10" fill="none" stroke="#fff" stroke-width="2"/>
    <path d="M112 20h20M122 10c-4 5-4 15 0 20M122 10c4 5 4 15 0 20" fill="none" stroke="#fff" stroke-width="1.6"/>
  </svg>
  <div class="abs contact" style="left:363px;top:362px;width:363px">hello@brickleafyardworks.com</div>
  <div class="abs contact" style="left:363px;top:400px;width:363px">4820 Cedar Hollow Rd Ste 210<br>Fairview, 77390, US</div>
  <div class="abs contact" style="left:363px;top:456px;width:363px">www.brickleafyardworks.com</div>

  <div class="abs brand" style="left:810px;top:54px"><span class="brand__dot"></span><span class="brand__name" style="font-size:22px">BRICKLEAF<br>YARDWORKS</span></div>
  <div class="abs" style="left:726px;top:528px;width:363px;text-align:center;line-height:1.1">
    <div style="color:var(--blue-light);font-weight:800;font-size:29px">Create</div>
    <div style="color:var(--green);font-weight:800;font-size:40px">YOUR DREAM</div>
    <div style="color:var(--blue);font-weight:800;font-size:29px">Backyard With Us</div>
  </div>
  <div class="abs phone-bar" style="left:765px;top:659px;width:284px;height:48px;font-size:29px">
    <svg width="24" height="24" viewBox="0 0 24 24"><path fill="#fff" d="M6.6 10.8a15.1 15.1 0 0 0 6.6 6.6l2.2-2.2a1 1 0 0 1 1-.25 11.4 11.4 0 0 0 3.6.57 1 1 0 0 1 1 1V20a1 1 0 0 1-1 1A17 17 0 0 1 3 4a1 1 0 0 1 1-1h3.5a1 1 0 0 1 1 1c0 1.25.2 2.45.57 3.57a1 1 0 0 1-.25 1z"/></svg>
    555-014-2297
  </div>
  <div class="abs contact" style="left:726px;top:718px;width:363px;font-weight:600">www.brickleafyardworks.com</div>
</section>

<section class="spread spread--inner" aria-label="Brochure inside spread">
  <svg class="art" width="1089" height="768" viewBox="0 0 1089 768">
    <defs>
      <linearGradient id="paperTone2" x1="0" y1="0" x2="0" y2="1">
        <stop offset="0" stop-color="#f4f5f5"/><stop offset="1" stop-color="#e5e8e8"/>
      </linearGradient>
      <linearGradient id="lawnPavilion" x1="0" y1="0" x2="0" y2="1">
        <stop offset="0" stop-color="#4f7a3a"/><stop offset=".35" stop-color="#9a6b48"/><stop offset=".7" stop-color="#5c9a38"/><stop offset="1" stop-color="#2a3a22"/>
      </linearGradient>
      <linearGradient id="patioLounge" x1="0" y1="0" x2="0" y2="1">
        <stop offset="0" stop-color="#a0714a"/><stop offset=".4" stop-color="#d9d6cf"/><stop offset=".75" stop-color="#b07a48"/><stop offset="1" stop-color="#7d7a74"/>
      </linearGradient>
      <linearGradient id="diningDeck" x1="0" y1="0" x2="1" y2="1">
        <stop offset="0" stop-color="#4d8a34"/><stop offset=".45" stop-color="#a0603e"/><stop offset=".75" stop-color="#6b4a34"/><stop offset="1" stop-color="#2f3134"/>
      </linearGradient>
    </defs>
    <rect width="1089" height="768" fill="url(#paperTone2)" role="img" aria-label="Faint backyard tree backdrop"/>
    <rect role="img" aria-label="Photo: cedar pavilion on green lawn" x="24" y="30" width="312" height="216" fill="url(#lawnPavilion)"/>
    <path d="M0 486C150 486 300 560 400 700L440 768" fill="none" stroke="var(--green)" stroke-width="7"/>
    <path d="M330 720C480 760 620 740 740 640" fill="none" stroke="var(--green)" stroke-width="7"/>
    <path role="img" aria-label="Photo: covered patio with chandelier and lounge seating" d="M0 500C150 500 290 570 385 705L420 768H0Z" fill="url(#patioLounge)"/>
    <g stroke="var(--blue)" stroke-width="4">
      <circle role="img" aria-label="Photo: round fire pit" cx="362" cy="648" r="62" fill="#7b7566"/>
      <circle role="img" aria-label="Photo: stone outdoor kitchen counter" cx="503" cy="648" r="62" fill="#6d6a66"/>
      <circle role="img" aria-label="Photo: fire pit seating in wooded yard" cx="642" cy="648" r="62" fill="#6b5a3e"/>
    </g>
    <path d="M690 0C695 120 735 200 800 242C880 292 1000 295 1089 270" fill="none" stroke="var(--blue)" stroke-width="9"/>
    <path role="img" aria-label="Photo: outdoor dining area with wall-mounted TV" d="M705 0H1089V258C1000 282 880 280 806 232C745 192 710 115 705 0Z" fill="url(#diningDeck)"/>
  </svg>

  <div class="abs" style="left:34px;top:212px;color:#fff;font-weight:800;font-size:25px">WHAT WE DO</div>
  <div class="abs heading" style="left:24px;top:262px;font-size:22px">Outdoor Kitchens</div>
  <div class="abs sub" style="left:24px;top:300px;width:310px">Immerse Yourself in the<br>World of Outdoor Kitchens</div>
  <p class="abs body" style="left:24px;top:352px;width:312px">Welcome to Brickleaf Yardworks, where we redefine outdoor living by bringing the heart of your home outdoors. Our focus on outdoor kitchens goes beyond functionality – we create immersive culinary spaces that elevate your outdoor living experience. Explore the possibilities and savor the joy of al fresco dining with our meticulously crafted outdoor kitchens.</p>

  <div class="abs heading" style="left:378px;top:26px;font-size:22px;line-height:1.32">Pavilions,<br>Patios<br>&amp; Pergola</div>
  <div class="abs sub" style="left:378px;top:126px;width:330px">Embrace Outdoor Elegance<br>with Pergolas and Patio Covers</div>
  <p class="abs body" style="left:378px;top:174px;width:320px">Welcome to Brickleaf Yardworks, where we specialize in creating outdoor spaces that seamlessly blend elegance, functionality, and tranquility. Our focus on pergolas and patio covers extends beyond providing shade; we craft architectural masterpieces that define and enhance your outdoor living experience. Discover the beauty and versatility of our pergolas and patio covers, designed to bring serenity to your backyard.</p>
  <div class="abs heading heading--green" style="left:380px;top:366px;font-size:22px">Fire Pits</div>
  <div class="abs sub" style="left:380px;top:405px;width:320px">Explore the Beauty of<br>Outdoor Fire Features</div>
  <p class="abs body" style="left:380px;top:456px;width:318px">At Brickleaf Yardworks, we transform ordinary outdoor spaces into extraordinary havens of warmth and ambiance. Our focus on outdoor fire features brings a touch of magic to your backyard, creating a space that invites relaxation, entertainment, and lasting memories.</p>

  <div class="abs heading" style="left:741px;top:293px;font-size:22px">Pools</div>
  <p class="abs body" style="left:741px;top:338px;width:320px;text-align:left">Our expert team will create a customized plan that brings together your</p>
  <div class="abs heading" style="left:741px;top:384px;font-size:22px">Landscaping &amp; Lighting</div>
  <p class="abs body" style="left:741px;top:432px;width:320px;text-align:left">Design a captivating backyard oasis with our landscaping and lighting service, harmonizing</p>
  <div class="abs process" style="left:744px;top:480px;width:324px;height:264px">
    <div class="process__title">EFFECTIVE PROCESS FOR<br>GREAT OUTCOMES</div>
    <ol class="process__list">
      <li><span class="process__num">01</span>TELL US ABOUT YOUR PROJECT</li>
      <li><span class="process__num">02</span>PHONE CONSULTATION</li>
      <li><span class="process__num">03</span>IN-PERSON CONSULTATION</li>
      <li><span class="process__num">04</span>DESIGN</li>
      <li><span class="process__num">05</span>CONSTRUCTION</li>
      <li><span class="process__num">06</span>POST CONSTRUCTION WALKTHROUGH</li>
    </ol>
  </div>
</section>

</body>
</html>
```